New small country town business wanting to expand online wants a website to do sales, post local ...

Our logo was designed through Pixel Harbor and we loved it. We would like a website designed for us. We want to be able to sell things online, manage the upkeep ourselves, have a separate page that we can advertise local businesses, a page that contains local information and events, local Buy, sell or swap page, promote tourism in our local area, chat with us. We use Quickbooks and Square We also have a local business Tallowind Creek Cruises - see our website for that www.tallowindcreekcruises.com.au which we promote through our shop 'The Reel Hut'. The Reel Hut sells, hot pies, fishing tackle, bait, groceries, boating accessories, souvenir T-Shirts (also designed by Pixel Harbor) etc. Do you set it up? Do I need to get the hosting done? I dont understand what coding the website means. I apologise for my ignorance. We sell coffee and newspapers to the locals. Provide a meeting place in a town where the only other shop here actively discourages and often verbally abuses the locals.Maree
I apologise for the delay, my father is in hospital and is gravely ill. I have had to fly to Perth to be with him . Can I please have a 2 week extension? Thank you. Mar ee

```html
<!DOCTYPE html>
<html lang="en">
<head>
<meta charset="utf-8">
<title>The Reel Hut</title>
<link rel="stylesheet" href="https://fonts.googleapis.com/css2?family=Poppins:wght@400;500;600;700;800&display=swap">
<style>
:root{
  --plank-a:#3d302b;
  --plank-b:#4b3c35;
  --plank-c:#33271f;
  --plank-d:#55453d;
  --gap:#1f1612;
  --panel:rgba(38,26,22,.74);
  --red:#b3151b;
  --white:#ffffff;
  --tan:#b9a58f;
  --blue:#7d97b6;
  --tab:#4a4644;
  --box-grey:rgba(200,196,194,.55);
}
*{margin:0;padding:0;box-sizing:border-box}
html,body{width:1200px;height:2294px;overflow:hidden}
body{
  position:relative;
  font-family:"Poppins",sans-serif;
  color:var(--white);
  background-color:var(--plank-a);
  background-image:
    repeating-linear-gradient(0deg,transparent 0 371px,rgba(0,0,0,.35) 371px 373px,transparent 373px 620px),
    repeating-linear-gradient(90deg,
      var(--plank-a) 0 38px,var(--gap) 38px 40px,
      var(--plank-b) 40px 78px,var(--gap) 78px 80px,
      var(--plank-c) 80px 118px,var(--gap) 118px 120px,
      var(--plank-d) 120px 158px,var(--gap) 158px 160px,
      var(--plank-b) 160px 198px,var(--gap) 198px 200px,
      var(--plank-c) 200px 238px,var(--gap) 238px 240px);
}
.abs{position:absolute}

/* nav */
.main-nav{left:188px;top:10px;display:flex;gap:7px;font-size:10.5px;font-weight:600;align-items:center}
.main-nav .sep{color:var(--red);font-size:10px}
.user-nav{right:188px;top:10px;display:flex;gap:14px;font-size:10.5px;font-weight:600;align-items:center}
.user-nav svg{vertical-align:-2px;margin-right:4px}

/* header */
.shop-info{left:188px;top:49px;width:326px;height:119px;background:var(--box-grey);
  text-align:center;font-size:11px;font-weight:700;line-height:18px;padding-top:12px;letter-spacing:-.2px}
.shop-info .red{color:var(--red)}
.shop-info p{margin-bottom:4px}
.brand-badge{left:574px;top:49px;width:122px;height:122px;border-radius:50%;background:var(--white);
  display:flex;align-items:center;justify-content:center;box-shadow:0 2px 6px rgba(0,0,0,.4)}
.brand-badge span{color:var(--red);font-weight:700;font-size:16px;text-align:center;line-height:1.1}
.call-out{left:764px;top:104px;transform:rotate(-12deg);transform-origin:left top;font-weight:800;font-size:18px;line-height:24px;white-space:nowrap}
.call-out .phone{display:inline-block;background:var(--white);color:var(--red);padding:0 6px;margin-left:4px}
.call-out .line2{display:block;padding-left:52px}

/* hero */
.hero{left:173px;top:202px;width:854px;height:374px;
  background:
    radial-gradient(ellipse 120px 90px at 660px 110px,rgba(235,225,215,.75),transparent),
    radial-gradient(ellipse 160px 120px at 380px 330px,rgba(220,180,160,.45),transparent),
    linear-gradient(100deg,#d4d0c8 0%,#b4aea5 38%,#6a4a34 58%,#2e1f18 80%,#1c130f 100%)}
.hero h1{position:absolute;left:34px;top:123px;font-size:26.5px;font-weight:800;line-height:27px;text-transform:uppercase;text-shadow:0 1px 3px rgba(0,0,0,.35)}
.btn{display:inline-block;background:var(--red);color:var(--white);font-size:10px;font-weight:700;text-transform:uppercase;
  height:37px;line-height:37px;width:91px;text-align:center}
.hero .btn{position:absolute;left:34px;top:223px}

/* about */
.about{left:173px;top:603px;width:854px;height:131px;background:var(--panel);padding:20px 22px 0}
.about h2,.section-title{font-size:25px;font-weight:800;text-transform:uppercase;text-align:center;line-height:30px}
.about p{font-size:12px;line-height:18px;margin-top:8px;font-weight:500;letter-spacing:-.15px}

/* products */
.product-card{width:263px;height:239px;padding:52px 9px 0}
.product-card.tan{background:var(--tan)}
.product-card.blue{background:var(--blue)}
.product-card .label{position:absolute;left:50%;top:9px;transform:translateX(-50%) rotate(-2deg);
  background:var(--tab);color:var(--white);font-size:13px;font-weight:700;text-transform:uppercase;
  padding:5px 12px;white-space:nowrap}
.product-card .label.tilt-r{transform:translateX(-50%) rotate(2deg)}
.product-card .photo{width:245px;height:178px;border:3px solid var(--white)}

/* charter */
.charter{left:173px;top:1293px;width:854px;height:343px;background:var(--panel)}
.charter .photo{position:absolute;left:22px;top:23px;width:393px;height:297px;border:3px solid var(--white);
  background:
    radial-gradient(ellipse 150px 60px at 210px 175px,rgba(250,250,250,.9),transparent),
    linear-gradient(180deg,#4f86cf 0%,#a9c4e6 35%,#5f6f4f 52%,#2f5582 60%,#1c3558 100%)}
.charter h2{position:absolute;left:438px;top:55px;width:400px;font-size:26.5px;font-weight:800;line-height:27px;text-transform:uppercase}
.charter p{position:absolute;left:438px;top:153px;width:400px;font-size:12px;line-height:18px;font-weight:500}
.charter .btn{position:absolute;left:438px;top:234px}

/* attractions */
.attractions{left:173px;top:1663px;width:854px;height:379px;background:var(--panel)}
.attractions .section-title{margin-top:19px}
.attraction{position:absolute;top:66px;width:215px;text-align:center}
.attraction .photo{width:215px;height:207px}
.attraction h3{font-size:13.5px;font-weight:700;margin-top:8px}
.attractions .btn{position:absolute;left:381px;top:315px}

/* footer */
.footer-badge{left:548px;top:2095px;width:102px;height:102px;border-radius:50%;background:var(--white);
  display:flex;align-items:center;justify-content:center;box-shadow:0 2px 6px rgba(0,0,0,.4)}
.footer-badge span{color:var(--red);font-weight:700;font-size:13px;text-align:center;line-height:1.1}
.social{left:545px;top:2216px;display:flex;gap:22px}
.social i{display:block;width:11px;height:11px;border-radius:2px;border:1.5px solid var(--white)}
.copyright{left:0;top:2263px;width:1200px;text-align:center;font-size:12px}
</style>
</head>
<body>

<nav class="abs main-nav">
  <span>HOME</span><span class="sep">★</span><span>ABOUT US</span><span class="sep">★</span>
  <span>PRODUCTS</span><span class="sep">★</span><span>NEWS</span><span class="sep">★</span><span>CONTACT US</span>
</nav>
<div class="abs user-nav">
  <span><svg width="9" height="10" viewBox="0 0 9 10"><circle cx="4.5" cy="2.6" r="2.4" fill="#b3151b"/><path d="M0 10c0-3 2-4.5 4.5-4.5S9 7 9 10z" fill="#b3151b"/></svg>MY ACCOUNT</span>
  <span><svg width="11" height="10" viewBox="0 0 11 10"><path d="M0 1h2l1.5 5h6L11 2H3" fill="none" stroke="#fff" stroke-width="1.4"/><circle cx="4" cy="8.5" r="1" fill="#fff"/><circle cx="9" cy="8.5" r="1" fill="#fff"/></svg>$0.00</span>
</div>

<div class="abs shop-info">
  <p>CAFE : COFFEE &amp; NEWSPAPER <span class="red">YOUR MEETING PLACE<br>IN TOWN</span> WE SELL: FOR YOUR BOAT TRIP</p>
  <p class="red">HOT PIES, FISHING TACKLE, BAIT, GROCERIES,<br>BOATING ACCESSORIES, SOUVENIR T-SHIRTS</p>
  <p>P.O. BOX 417 MARLOW BAY NSW 2290</p>
</div>
<div class="abs brand-badge"><span>The Reel Hut</span></div>
<div class="abs call-out">PLEASE CALL<span class="phone">0400 118 264</span><span class="line2">....FOR ENQUIRIES</span></div>

<section class="abs hero" role="img" aria-label="Photo of a person reading a newspaper beside a cappuccino and a slice of cake">
  <h1>Providing a meeting<br>place in town with<br>coffee and newspaper</h1>
  <a class="btn">Read more</a>
</section>

<section class="abs about">
  <h2>About Us</h2>
  <p>Duis aute irure dolor in reprehenderit in voluptate velit esse cillum dolore eu fugiat nulla pariatur. Excepteur sint occaecat cupidatat non proident, sunt in culpa qui officia deserunt mollit anim id est laborum. Neque porro quisquam est, qui dolorem ipsum quia dolor sit amet, consectetur, adipisci velit, sed quia non numquam eius modi tempora</p>
</section>

<div class="abs product-card tan" style="left:183px;top:761px"><span class="label">Hot Pies</span>
  <div class="photo" role="img" aria-label="Photo of golden hot pies in foil trays" style="background:radial-gradient(circle at 45% 40%,#f2c060,#d58a2a 45%,#8a4a14)"></div></div>
<div class="abs product-card blue" style="left:468px;top:761px"><span class="label tilt-r">Fishing Tackle</span>
  <div class="photo" role="img" aria-label="Photo of fishing rods and reels on a wooden deck" style="background:linear-gradient(160deg,#7a6a52,#4a3d30 50%,#2c241d)"></div></div>
<div class="abs product-card tan" style="left:754px;top:761px"><span class="label">Bait</span>
  <div class="photo" role="img" aria-label="Photo of colourful fishing lures on display" style="background:linear-gradient(160deg,#cfd8cf 0%,#e3b33a 30%,#3a7fc0 55%,#c8d4c8 100%)"></div></div>

<div class="abs product-card blue" style="left:183px;top:1027px"><span class="label tilt-r">Groceries</span>
  <div class="photo" role="img" aria-label="Photo of a shopper choosing fresh fruit in a grocery aisle" style="background:linear-gradient(120deg,#e09a35,#8a9a3c 40%,#d04a3c 70%,#d8d2c8)"></div></div>
<div class="abs product-card tan" style="left:468px;top:1027px"><span class="label">Boating Accessories</span>
  <div class="photo" role="img" aria-label="Photo of fishing reels, line spools and a tackle box" style="background:linear-gradient(140deg,#3e3e3e,#6a6a6a 35%,#2f7e74 65%,#c9b13a)"></div></div>
<div class="abs product-card blue" style="left:754px;top:1027px"><span class="label tilt-r">Souvenir T-Shirts</span>
  <div class="photo" role="img" aria-label="Photo of a navy souvenir T-shirt" style="background:linear-gradient(90deg,#b9b2a4,#1f2a4a 20%,#243258 60%,#1f2a4a 80%,#a49a8a)"></div></div>

<section class="abs charter">
  <div class="photo" role="img" aria-label="Photo of a white cruiser boat moored on a calm river"></div>
  <h2>Easy access to the stunning Tallowind Creek Cruises</h2>
  <p>Our spencer base is only a little over an hour from the north shore of sydney in the centre of the majestic tallowind creek between brooklyn and wisemans ferry.</p>
  <a class="btn">Read more</a>
</section>

<section class="abs attractions">
  <h2 class="section-title">Tourist Attractions</h2>
  <div class="attraction" style="left:42px">
    <div class="photo" role="img" aria-label="Photo of wildlife in a gum tree at the park" style="background:linear-gradient(160deg,#b8c0a8,#7c8a5a 40%,#4f5d3a)"></div>
    <h3>Gumleaf Wildlife Park</h3></div>
  <div class="attraction" style="left:320px">
    <div class="photo" role="img" aria-label="Photo of vegetable rows on a farm" style="background:repeating-linear-gradient(170deg,#4d7a5e 0 18px,#8a5a48 18px 26px,#6f8a52 26px 40px)"></div>
    <h3>Bracken Hill Farm</h3></div>
  <div class="attraction" style="left:597px">
    <div class="photo" role="img" aria-label="Photo of a sandstone chapel among trees" style="background:linear-gradient(180deg,#3b7fd0,#6ea0da 30%,#c9955a 55%,#3a4a2a)"></div>
    <h3>Stonebridge Chapel</h3></div>
  <a class="btn">Read more</a>
</section>

<div class="abs footer-badge"><span>The Reel Hut</span></div>
<div class="abs social" aria-label="Social links"><i></i><i></i><i></i><i></i></div>
<p class="abs copyright">Copyright © 2019 The Reel Hut</p>

</body>
</html>
```